Zumbly - New Payment App for Student

Zum-bly - A Payment App for student to make payment, track own expenses and practice good dietary habits. The App theme is Fun and excitement.
Target User: Secondary Student aged 13-18
Look and Feel: Fun, excitement and simple.
Screen 1
Login to the app using thumbprints or password
Screen 2
Display the balance
Wallet balance >>> go to screen 3 to display transaction history
Gamification balance - points + badges >>> go to screen 3
Button to make payment
Screen 2-1
Allow them to do payment
Click “Pay”
Display QR code
scanning by merchant
Payment made
Notification received
The transaction history will be shown up
Screen 2-2
Allow them to top up (alternatively to parent Top-up using credit card)
Click “Top Up”
Display QR code
Pass the cash to merchant
scanning by merchant
Payment made
Notification received
The new balance will be shown up
Screen 3
Display more details on transaction history
Payment history + gamification history (gain/redeem points)
E.g. 14 Nov Canteen purchase $5.40
- Banana +30 points
- Milk +10 points
Screen 4 (play a game to earn point)
Introduce some trivial games (while waiting in line at cafeteria or school store) to gain some points
Crosswords
Puzzle
Screen 5 (Display achievements)
Leaderboard
Where the individual stands in the class
Where the class stands overall in school
Badges
Level
Achievements
For more, please go to our website http://www.zumbly-pay.example/
Target Market(s)
Secondary School Student aged 13-18
Industry/Entity Type
Education
Logo Text
zumbly
Look and feel

```html
<!DOCTYPE html>
<html lang="en">
<head>
<meta charset="utf-8">
<title>Zumbly – Home</title>
<link href="https://fonts.googleapis.com/css2?family=Inter:wght@400;500&display=swap" rel="stylesheet">
<style>
  :root {
    --brand-purple: #6b4bcc;
    --screen-bg: #232428;
    --tap-circle: #38393d;
    --tap-text: #9b9ca1;
    --white: #ffffff;
    --coin: #f2b91d;
    --coin-dark: #d99a12;
    --shield: #f5b400;
    --star: #ffe14a;
    --avatar-pink: #f29ac8;
  }
  * { margin: 0; padding: 0; box-sizing: border-box; }
  html, body { width: 675px; height: 1200px; overflow: hidden; }
  body {
    font-family: "Inter", sans-serif;
    background: var(--screen-bg);
    position: relative;
    color: var(--white);
  }
  .app-header {
    position: absolute; left: 0; top: 0;
    width: 675px; height: 272px;
    background: var(--brand-purple);
  }
  .status-bar {
    position: absolute; left: 0; top: 0; width: 675px; height: 36px;
    font-size: 18px; font-weight: 400;
  }
  .status-bar .signal { position: absolute; left: 11px; top: 11px; }
  .status-bar .time { position: absolute; left: 0; width: 675px; top: 8px; text-align: center; }
  .status-bar .battery-label { position: absolute; right: 66px; top: 8px; }
  .status-bar .battery { position: absolute; right: 13px; top: 10px; }
  .avatar {
    position: absolute; left: 25px; top: 104px;
    width: 136px; height: 108px;
    border-radius: 50% 50% 46% 46%;
    background: radial-gradient(circle at 50% 45%, #f7b6d8, var(--avatar-pink) 70%, #d975ad);
  }
  .welcome {
    position: absolute; left: 195px; top: 98px;
    font-size: 36px; font-weight: 500; letter-spacing: 0.2px;
  }
  .stat {
    position: absolute; top: 172px;
    display: flex; align-items: center; gap: 14px;
    font-size: 23px; font-weight: 500;
  }
  .stat.points { left: 194px; }
  .stat.badges { left: 424px; }
  .leaderboard-icon { position: absolute; left: 585px; top: 92px; }
  .tap-button {
    position: absolute; left: 200px; top: 601px;
    width: 275px; height: 275px; border-radius: 50%;
    background: var(--tap-circle);
    display: flex; align-items: center; justify-content: center;
    color: var(--tap-text);
    font-size: 42px; font-weight: 400;
  }
</style>
</head>
<body>
  <header class="app-header">
    <div class="status-bar">
      <svg class="signal" width="92" height="16" viewBox="0 0 92 16">
        <g fill="#fff">
          <circle cx="5" cy="7" r="4.5"/><circle cx="16" cy="7" r="4.5"/><circle cx="27" cy="7" r="4.5"/>
          <circle cx="38" cy="7" r="4.5"/><circle cx="49" cy="7" r="4.5"/>
        </g>
        <g fill="none" stroke="#fff" stroke-width="2.4" stroke-linecap="round">
          <path d="M62 5 a14 14 0 0 1 20 0"/><path d="M65.5 8.5 a9 9 0 0 1 13 0"/>
        </g>
        <circle cx="72" cy="13" r="2.2" fill="#fff"/>
      </svg>
      <div class="time">9:41 AM</div>
      <div class="battery-label">100%</div>
      <svg class="battery" width="46" height="18" viewBox="0 0 46 18">
        <rect x="1" y="1" width="40" height="16" rx="3" fill="none" stroke="#fff" stroke-width="1.6"/>
        <rect x="3.5" y="3.5" width="35" height="11" rx="1.5" fill="#fff"/>
        <rect x="42.5" y="6" width="2.5" height="6" rx="1" fill="#fff"/>
      </svg>
    </div>

    <div class="avatar" role="img" aria-label="Player avatar: a cute round pink character"></div>

    <h1 class="welcome">Welcome Arjun</h1>

    <div class="stat points">
      <svg width="34" height="36" viewBox="0 0 34 36" aria-hidden="true">
        <g stroke="var(--coin-dark)" stroke-width="1.5" fill="var(--coin)">
          <ellipse cx="17" cy="29" rx="15" ry="5"/>
          <ellipse cx="17" cy="23" rx="15" ry="5"/>
          <ellipse cx="17" cy="17" rx="15" ry="5"/>
          <ellipse cx="17" cy="11" rx="13" ry="4.5"/>
          <ellipse cx="17" cy="6" rx="11" ry="4"/>
        </g>
      </svg>
      <span>750 Points</span>
    </div>

    <div class="stat badges">
      <svg width="35" height="38" viewBox="0 0 35 38" aria-hidden="true">
        <path d="M17.5 1 L33 6 V18 C33 28 26 34 17.5 37 C9 34 2 28 2 18 V6 Z" fill="var(--shield)"/>
        <path d="M17.5 10 l2.6 5.3 5.8 .8 -4.2 4.1 1 5.8 -5.2 -2.7 -5.2 2.7 1 -5.8 -4.2 -4.1 5.8 -.8z" fill="var(--star)"/>
      </svg>
      <span>3 Badges</span>
    </div>

    <svg class="leaderboard-icon" width="67" height="44" viewBox="0 0 67 44" aria-label="Leaderboard" role="img">
      <g fill="#fff">
        <rect x="0" y="14" width="22" height="30" rx="1"/>
        <rect x="22" y="0" width="23" height="44" rx="1"/>
        <rect x="45" y="20" width="22" height="24" rx="1"/>
      </g>
      <g fill="var(--brand-purple)" font-family="Inter, sans-serif" font-size="12" font-weight="500" text-anchor="middle">
        <text x="11" y="28">2</text><text x="33.5" y="14">1</text><text x="56" y="34">3</text>
      </g>
    </svg>
  </header>

  <div class="tap-button">Tap Here</div>
</body>
</html>
```